Retail Label Design - Hand Sanitizer

BRISKEN is Volkmar Norths legacy brand. For decades Volkmar North has been trusted by our customers to provide unmatched capability in the revitalization of surfaces and materials. We are proud to relaunch BRISKENTM with the same promise, but oriented towards a new challenge: meeting the demand for solutions to aid in our collective fight against COVID-19.

BRISKENTM Ethanol Hand Sanitizer is the first official relaunch product – and 80% alcohol based sanitizer, free from fragrance and dye.

We want to maintain a cool and clean feel for the labels – reflective of the product. Ideally if we could incorporate a retro feel to the packaging, we would be very happy.

This label will need to be done to 3 different specs to suit a 235ml, 500ml and 4L package. We would like to start with the 500ml label. I have attached the dieline, (774-QZL) for the 500ml Package. I have also attached product info, logo and brand info.

The only requirements on the front panel is the logo, product name (Ethanol Gel Hand Sanitizer) and the quantity(473ml), space for barcode on back + info provided. the rest we will leave up to your expertise.

Font styles to use
Serif
Sans Serif

Requirements
Must have
• Logo
Product name
Quantity
Information on back panel provided.

```html
<!DOCTYPE html>
<html lang="en">
<head>
<meta charset="utf-8">
<title>BRISKEN Ethanol Gel Hand Sanitizer – Label</title>
<link rel="stylesheet" href="https://fonts.googleapis.com/css2?family=Saira:wght@400;500;600;700&family=Saira+Semi+Condensed:wght@400;500&display=swap">
<style>
  :root {
    --bg: #f4efe6;
    --navy: #2e3d4d;
    --teal-deep: #3f7f84;
    --teal: #9fdcdc;
    --teal-soft: #c9ecea;
    --white: #ffffff;
    --splash: #7cc9c9;
  }
  * { box-sizing: border-box; margin: 0; padding: 0; }
  html, body {
    width: 1200px; height: 800px; overflow: hidden;
    background: var(--bg);
  }
  .canvas {
    position: relative; width: 1200px; height: 800px;
    display: flex; justify-content: center; align-items: center; gap: 60px;
  }
  .label {
    position: relative; width: 360px; height: 510px; overflow: hidden;
    background: linear-gradient(180deg, var(--teal) 0%, var(--teal-soft) 40%, var(--white) 70%, var(--white) 100%);
    color: var(--navy);
    font-family: "Saira", sans-serif;
    box-shadow: 0 10px 30px rgba(60, 50, 30, 0.12);
  }
  .brand-name {
    font-family: "Saira", sans-serif; font-weight: 700;
    color: var(--navy); letter-spacing: 2px; text-align: center;
  }
  .front .brand-name { position: absolute; top: 78px; width: 100%; font-size: 48px; }
  .front .product-name {
    position: absolute; top: 200px; width: 100%; text-align: center;
    font-weight: 500; font-size: 27px; line-height: 1.25; letter-spacing: 1.5px;
    color: var(--teal-deep);
  }
  .front .product-name span { color: var(--navy); }
  .water-art {
    position: absolute; left: 0; bottom: 0; width: 100%; height: 200px;
    background:
      radial-gradient(ellipse 18% 22% at 50% 30%, rgba(124, 201, 201, 0.9), rgba(124, 201, 201, 0) 70%),
      radial-gradient(ellipse 80% 30% at 50% 78%, rgba(124, 201, 201, 0.7), rgba(255, 255, 255, 0) 75%);
  }
  .quantity {
    position: absolute; bottom: 16px; width: 100%; text-align: center;
    font-weight: 600; font-size: 18px; letter-spacing: 1px;
  }
  .back .brand-name { margin-top: 34px; font-size: 28px; }
  .back .product-title {
    text-align: center; font-weight: 500; font-size: 17px; letter-spacing: 1px;
    margin-top: 10px;
  }
  .info { padding: 22px 24px 0; }
  .info-block { margin-bottom: 14px; }
  .info-heading {
    font-weight: 600; font-size: 12px; letter-spacing: 1px; text-transform: uppercase;
    margin-bottom: 4px;
  }
  .info-text {
    font-family: "Saira Semi Condensed", sans-serif;
    font-size: 10.5px; line-height: 1.35; letter-spacing: 0.3px;
  }
  .back .water-art { height: 110px; opacity: 0.6; }
  .back-footer {
    position: absolute; left: 24px; right: 24px; bottom: 16px;
    display: flex; justify-content: space-between; align-items: baseline;
  }
  .origin { font-size: 8.5px; font-weight: 600; letter-spacing: 0.6px; text-transform: uppercase; }
  .back .quantity { position: static; width: auto; font-size: 12px; }
</style>
</head>
<body>
<main class="canvas">
  <section class="label front">
    <div class="brand-name">BRISKEN</div>
    <h1 class="product-name">ETHANOL<br><span>GEL HAND SANITIZER</span></h1>
    <div class="water-art" role="img" aria-label="Illustration of a water droplet falling into a splashing wave"></div>
    <div class="quantity">235 ml</div>
  </section>

  <section class="label back">
    <div class="brand-name">BRISKEN</div>
    <h2 class="product-title">ETHANOL GEL HAND SANITIZER</h2>
    <div class="info">
      <div class="info-block">
        <h3 class="info-heading">Description:</h3>
        <p class="info-text">BRISKENTM Ethanol Hand Sanitizer is 80% alcohol based, perfume and dye free. Kills many common germs in seconds, when soap and water are not available and evaporates completely without the need to rinse. Recommended for repeated use.</p>
      </div>
      <div class="info-block">
        <h3 class="info-heading">Usage:</h3>
        <p class="info-text">Ideal for outside the washroom to provide hand hygiene at the work-point or on the move. Ideal for schools, offices, public facilities and more.</p>
      </div>
      <div class="info-block">
        <h3 class="info-heading">Method of use:</h3>
        <p class="info-text">Apply directly to hands and rub over your nails, into your palms and between your fingers, for 30sec, until completely dry.</p>
      </div>
      <div class="info-block">
        <h3 class="info-heading">Handling instructions:</h3>
        <p class="info-text">In case of contact with eyes, rinse immediately with water for at least ten minutes. Children under 6 years of age should be supervised when using this product. This product has a shelf life of one year from the date of manufacture.</p>
      </div>
    </div>
    <div class="water-art" role="img" aria-label="Faint water wave illustration"></div>
    <div class="back-footer">
      <span class="origin">Manufactured and packaged in Ontario, Canada.</span>
      <span class="quantity">235 ml</span>
    </div>
  </section>
</main>
</body>
</html>
```